Business card for medical clinic

I need an upmarket, modern medical/health business card for my clinic

Contact Information for Business Card

name, address, email, qr code

```html
<!DOCTYPE html>
<html lang="en">
<head>
<meta charset="utf-8">
<title>Meridia Health Partners – Business Card</title>
<link href="https://fonts.googleapis.com/css2?family=Cinzel:wght@500&family=Arimo:wght@400&display=swap" rel="stylesheet">
<style>
  :root {
    --backdrop: #2b2b2d;
    --card-front: #ffffff;
    --card-back: #333335;
    --emblem-back: #2c2c2e;
    --emblem-front: #2b86c4;
    --brand-blue: #1f6fa8;
    --brand-blue-light: #2b86c4;
    --text-light: #f2f2f2;
  }
  * { box-sizing: border-box; margin: 0; padding: 0; }
  html, body {
    width: 1200px; height: 689px; overflow: hidden;
    background: var(--backdrop);
  }
  .canvas {
    position: relative; width: 1200px; height: 689px;
    display: flex; align-items: center; justify-content: center; gap: 60px;
  }
  .card {
    width: 520px; height: 300px; border-radius: 18px;
    position: relative; overflow: hidden;
    box-shadow: 0 14px 30px rgba(0,0,0,0.45);
  }
  .card--front {
    background: var(--card-front);
    display: flex; align-items: center; justify-content: center; gap: 18px;
  }
  .brand-mark {
    width: 56px; height: 56px; border-radius: 50%;
    background: var(--emblem-front);
    flex-shrink: 0;
  }
  .brand-name {
    font-family: "Cinzel", serif; font-weight: 500;
    color: var(--brand-blue);
    letter-spacing: 0.04em; line-height: 1.15;
  }
  .card--front .brand-name { font-size: 30px; }
  .card--back {
    background: var(--card-back);
    padding: 48px 0 0 44px;
  }
  .back-emblem {
    position: absolute; right: 36px; top: 34px;
    width: 230px; height: 230px; border-radius: 50%;
    background: var(--emblem-back);
  }
  .back-content { position: relative; width: 240px; }
  .card--back .brand-name { font-size: 17px; margin-bottom: 26px; white-space: nowrap; }
  .person-name {
    font-family: "Cinzel", serif; font-weight: 500;
    font-size: 24px; color: var(--brand-blue-light);
    letter-spacing: 0.03em; white-space: nowrap;
  }
  .person-role, .address, .contact-list {
    font-family: "Arimo", sans-serif; color: var(--text-light);
    font-size: 13px; line-height: 1.4;
  }
  .person-role { margin-bottom: 12px; }
  .address { margin-bottom: 12px; }
  .contact-list { list-style: none; }
  .contact-list li { display: flex; align-items: center; gap: 10px; }
  .contact-icon { width: 12px; height: 12px; flex-shrink: 0; }
  .contact-icon * { fill: none; stroke: var(--brand-blue-light); stroke-width: 1.6; }
</style>
</head>
<body>
<main class="canvas">
  <section class="card card--front" aria-label="Card front">
    <span class="brand-mark" aria-hidden="true"></span>
    <div class="brand-name">Meridia Health<br>Partners</div>
  </section>

  <section class="card card--back" aria-label="Card back">
    <div class="back-emblem" role="img" aria-label="Large embossed brand emblem"></div>
    <div class="back-content">
      <div class="brand-name">Meridia Health Partners</div>
      <div class="person-name">Daniel Reyes</div>
      <div class="person-role">President</div>
      <div class="address">2145 Linden Avenue<br>Halford, Canada 58210</div>
      <ul class="contact-list">
        <li>
          <svg class="contact-icon" viewBox="0 0 12 12" aria-hidden="true"><path d="M2 1.5 L4.2 1.5 L5 4 L3.6 5 Q4.8 7.4 7 8.4 L8 7 L10.5 7.8 L10.5 10 Q5.5 10.5 1.5 2 Z"/></svg>
          555-210-4471
        </li>
        <li>
          <svg class="contact-icon" viewBox="0 0 12 12" aria-hidden="true"><rect x="3" y="1" width="6" height="10" rx="1"/></svg>
          555-318-9026
        </li>
        <li>
          <svg class="contact-icon" viewBox="0 0 12 12" aria-hidden="true"><rect x="1" y="2.5" width="10" height="7"/><path d="M1 2.5 L6 6.5 L11 2.5"/></svg>
          info@meridiahealth.com
        </li>
        <li>
          <svg class="contact-icon" viewBox="0 0 12 12" aria-hidden="true"><circle cx="6" cy="6" r="5"/><path d="M1 6 H11 M6 1 Q3 6 6 11 Q9 6 6 1"/></svg>
          www.meridiahealth.com
        </li>
      </ul>
    </div>
  </section>
</main>
</body>
</html>
```